Web Design Project

This web site is to be designed for a popular Cambodian singer, Vanny Kolthida. Web site name "Vanny Kolthida".

The purpose is to keep her fans update with the latest of her entertainment career and invite them to help raising fund for Lotus Bridge Youth Fund.

In addition to other normal pages such as HOME, ABOUT... This web site must be:
1. able to link to Dropshipers and add Products
2. able to donate (accept Major Credit Cards or PayVira)
3. able to purchase products (accept Major Credit Cards or PayVira)
4. able to video live chat with Vanny Kolthida
5. able to book appointment on her calendar

Here is a sample of the web site:
http://pralay82.sitebuildo.example/vanny-kol-thida

Please call me if you need any clarification at 1-555-281-3097 or leave your number for me to call you back.

Thank you

Dara

Target Market(s)

Cambodian living abroad

Industry/Entity Type

Entertainment

Requirements
Must have
• 1. able to link to Dropshipers and add Products
2. able to Donate (accept Major Credit Cards or PayVira)

```html
<!DOCTYPE html>
<html lang="en">
<head>
<meta charset="utf-8">
<title>Vanny Kolthida</title>
<link rel="stylesheet" href="https://fonts.googleapis.com/css2?family=Michroma&family=Roboto+Condensed:wght@400;700&family=Arimo:wght@400;700&display=swap">
<style>
:root{
  --black:#000;
  --purple:#8e1480;
  --purple-deep:#4a0a45;
  --lime:#c8e80e;
  --yellow:#e8e015;
  --pink:#e2138e;
  --gold:#f3b400;
  --grey:#9a9a9a;
  --text:#cfcfcf;
  --link:#c866c0;
}
*{margin:0;padding:0;box-sizing:border-box}
html,body{width:1200px;height:890px;overflow:hidden;background:var(--black)}
.page{position:relative;width:1200px;height:890px;overflow:hidden;font-family:Arimo,sans-serif;color:#fff;
  background:
    radial-gradient(ellipse 420px 330px at 250px 330px,rgba(170,20,150,.95),rgba(120,10,110,.6) 45%,transparent 80%),
    radial-gradient(ellipse 380px 300px at 1060px 230px,rgba(200,200,10,.95),rgba(140,140,0,.5) 50%,transparent 85%),
    linear-gradient(180deg,#3a1a30 0,#000 60%);}
.shape{position:absolute;background:rgba(255,255,255,.07);clip-path:polygon(50% 0,100% 38%,82% 100%,18% 100%,0 38%)}
.header{position:absolute;left:0;top:0;width:1200px;height:73px;background:rgba(0,0,0,.35)}
.brand{position:absolute;left:187px;top:24px;font-family:Michroma,sans-serif;font-size:30px;font-weight:400;color:#fff;letter-spacing:1px}
.datetime{position:absolute;left:680px;top:20px;width:470px;height:32px;background:rgba(0,0,0,.35);font-family:'Roboto Condensed',sans-serif;font-size:17px;padding:6px 0 0 28px}
.nav{position:absolute;left:0;top:73px;width:1200px;height:28px;background:#000;font-family:'Roboto Condensed',sans-serif;font-size:17px}
.nav a{position:absolute;top:4px;color:#fff;text-decoration:none}
.nav .active{left:166px;top:0;width:100px;height:28px;background:var(--purple);text-align:center;padding-top:4px}
.card{position:absolute;top:120px;width:165px;height:146px;border-radius:3px;background:linear-gradient(180deg,#dcdcdc,#8a8a8a)}
.card .photo{position:absolute;left:4px;top:5px;width:157px;height:87px}
.card .label{position:absolute;left:17px;top:111px;font-size:16px;font-weight:700;text-decoration:underline}
.card svg{position:absolute;right:15px;top:112px}
.events{position:absolute;left:167px;top:294px;width:367px}
.event{position:relative;height:77px;border-bottom:1px solid #333}
.event .num{position:absolute;left:12px;top:10px;font-size:16px}
.event .date{position:absolute;left:55px;top:10px;font-size:12px;color:var(--yellow)}
.event .name{position:absolute;left:55px;top:26px;font-size:11px}
.event .djs{position:absolute;left:55px;top:45px;font-size:8.5px;letter-spacing:1px;color:#ccc}
.event svg{position:absolute;right:34px;top:20px}
.more{position:absolute;font-size:11px;font-weight:700;color:var(--link);text-decoration:underline}
.clip{position:absolute;left:168px;top:729px;width:390px;height:139px;border:3px solid #b4b010;background:linear-gradient(135deg,#5a6a90,#a08060 50%,#605070)}
.player{position:absolute;left:571px;top:294px;width:459px;height:235px;border:3px solid #ddd;background:#000}
.player h2{position:absolute;right:32px;top:148px;font-size:21px;color:var(--lime)}
.player p{position:absolute;right:20px;top:178px;font-size:10.5px;text-align:right;line-height:12px}
.player .bar{position:absolute;left:0;bottom:0;width:100%;height:18px;background:#1c1c1c;border-top:3px solid #444;font-size:6px;color:#aaa;padding:4px 0 0 46px}
.welcome{position:absolute;left:580px;top:556px;font-size:22px;font-weight:700;color:var(--yellow)}
.intro{position:absolute;left:581px;top:592px;width:440px;font-size:11px;line-height:15.7px;color:var(--text)}
.promo{position:absolute;top:747px;width:208px;height:119px;font-size:19px;font-weight:700;line-height:21px;padding:58px 0 0 16px}
.promo.gold{left:584px;background:linear-gradient(135deg,#f9d300,#efa200);color:#fff8c0}
.promo.pink{left:822px;background:linear-gradient(135deg,#f24bb0,#d80a80);color:#fff}
.promo .icon{position:absolute;left:24px;top:-42px;width:70px;height:70px;border-radius:50%}
.promo svg{position:absolute;right:26px;top:-14px}
</style>
</head>
<body>
<div class="page">
  <div class="shape" style="left:80px;top:30px;width:120px;height:110px"></div>
  <div class="shape" style="left:610px;top:0;width:80px;height:60px"></div>
  <div class="shape" style="left:1050px;top:110px;width:110px;height:110px"></div>
  <div class="shape" style="left:300px;top:270px;width:110px;height:110px"></div>
  <div class="shape" style="left:430px;top:480px;width:80px;height:80px"></div>
  <div class="shape" style="left:955px;top:510px;width:80px;height:80px"></div>

  <header class="header">
    <div class="brand">VANNY KOLTHIDA</div>
    <div class="datetime">SUNDAY, NOVEMBER 18, 2012 AT 1:24:28 PM</div>
  </header>
  <nav class="nav">
    <a class="active" href="#">Home</a>
    <a href="#" style="left:308px">About</a>
    <a href="#" style="left:422px">Video</a>
    <a href="#" style="left:533px">Store</a>
    <a href="#" style="left:642px">Live Chat</a>
  </nav>

  <div class="card" style="left:172px"><div class="photo" role="img" aria-label="Photo of the singer in a black jacket" style="background:linear-gradient(90deg,#bbb,#555)"></div><span class="label" style="color:#8e1480">home</span><svg width="20" height="20"><circle cx="10" cy="10" r="9" fill="#888" stroke="#eee" stroke-width="1.5"/><path d="M5 10h9M10 6l4 4-4 4" stroke="#fff" stroke-width="2" fill="none"/></svg></div>
  <div class="card" style="left:346px"><div class="photo" role="img" aria-label="Photo of the singer with a headband" style="background:linear-gradient(90deg,#ddd,#777)"></div><span class="label" style="color:#6a22b0">Video</span><svg width="20" height="20"><circle cx="10" cy="10" r="9" fill="#888" stroke="#eee" stroke-width="1.5"/><path d="M5 10h9M10 6l4 4-4 4" stroke="#fff" stroke-width="2" fill="none"/></svg></div>
  <div class="card" style="left:519px"><div class="photo" role="img" aria-label="Photo of the singer in a red dress" style="background:linear-gradient(90deg,#555,#b02020)"></div><span class="label" style="color:#4a0a45">parties</span><svg width="20" height="20"><circle cx="10" cy="10" r="9" fill="#888" stroke="#eee" stroke-width="1.5"/><path d="M5 10h9M10 6l4 4-4 4" stroke="#fff" stroke-width="2" fill="none"/></svg></div>
  <div class="card" style="left:692px"><div class="photo" role="img" aria-label="Black and white photo of the singer" style="background:linear-gradient(90deg,#333,#aaa)"></div><span class="label" style="color:#f0c400">store</span><svg width="20" height="20"><circle cx="10" cy="10" r="9" fill="#888" stroke="#eee" stroke-width="1.5"/><path d="M5 10h9M10 6l4 4-4 4" stroke="#fff" stroke-width="2" fill="none"/></svg></div>
  <div class="card" style="left:865px"><div class="photo" role="img" aria-label="Photo of the singer in a red cap" style="background:linear-gradient(90deg,#6a4a10,#b08a40)"></div><span class="label" style="color:#c8e80e">contacts</span><svg width="20" height="20"><circle cx="10" cy="10" r="9" fill="#888" stroke="#eee" stroke-width="1.5"/><path d="M5 10h9M10 6l4 4-4 4" stroke="#fff" stroke-width="2" fill="none"/></svg></div>

  <section class="events">
    <div class="event"><span class="num">01</span><span class="date">FEBRUARY 10</span><span class="name">EXPRESS PARTY</span><span class="djs">DJ LONDON , DJ FARRY</span><svg width="20" height="20"><circle cx="10" cy="10" r="9" fill="#666"/><path d="M5 10h9M10 6l4 4-4 4" stroke="#fff" stroke-width="2" fill="none"/></svg></div>
    <div class="event"><span class="num">02</span><span class="date">FEBRUARY 17</span><span class="name">EXPRESS PARTY</span><span class="djs">DJ LONDON , DJ FARRY</span><svg width="20" height="20"><circle cx="10" cy="10" r="9" fill="#666"/><path d="M5 10h9M10 6l4 4-4 4" stroke="#fff" stroke-width="2" fill="none"/></svg></div>
    <div class="event"><span class="num">03</span><span class="date">FEBRUARY 22</span><span class="name">EXPRESS PARTY</span><span class="djs">DJ LONDON , DJ FARRY</span><svg width="20" height="20"><circle cx="10" cy="10" r="9" fill="#666"/><path d="M5 10h9M10 6l4 4-4 4" stroke="#fff" stroke-width="2" fill="none"/></svg></div>
    <div class="event"><span class="num">04</span><span class="date">FEBRUARY 29</span><span class="name">EXPRESS PARTY</span><span class="djs">DJ LONDON , DJ FARRY</span><svg width="20" height="20"><circle cx="10" cy="10" r="9" fill="#666"/><path d="M5 10h9M10 6l4 4-4 4" stroke="#fff" stroke-width="2" fill="none"/></svg></div>
    <div class="event"><span class="num">05</span><span class="date">FEBRUARY 30</span><span class="name">EXPRESS PARTY</span><span class="djs">DJ LONDON , DJ FARRY</span><svg width="20" height="20"><circle cx="10" cy="10" r="9" fill="#666"/><path d="M5 10h9M10 6l4 4-4 4" stroke="#fff" stroke-width="2" fill="none"/></svg></div>
  </section>
  <a class="more" href="#" style="left:222px;top:688px">ALL SCHEDULE</a>

  <div class="clip" role="img" aria-label="Video still of a live stage performance with musicians"></div>

  <div class="player">
    <svg width="16" height="16" style="position:absolute;left:250px;top:84px"><circle cx="8" cy="8" r="6" fill="none" stroke="#777" stroke-width="2" stroke-dasharray="3 2"/></svg>
    <h2>Video 2012</h2>
    <p>Quisque in lacus. Pellentesque vitae en.im<br>quis ante hendrerit lobortis.</p>
    <div class="bar">00:00 / 25:36</div>
  </div>

  <h2 class="welcome">Welcome to our site!</h2>
  <p class="intro">In pharetra ipsum condimentum elit. Suspendisse mattis turpis eget odio. Class aptent taciti sociosqu ad litora torquent per conubia nostra, per inceptos hymenaeos. Pellentesque tempus dictum urna. Sed consequat massa eget metus. Quisque mollis pretium nisl. Mauris venenatis porttitor risus. Phasellus accumsan turpis. Nam sagittis nulla quis orci.</p>
  <a class="more" href="#" style="left:581px;top:676px">READ MORE</a>

  <div class="promo gold"><div class="icon" role="img" aria-label="Loudspeaker icon" style="background:radial-gradient(circle,#666,#ccc)"></div><svg width="50" height="50"><circle cx="25" cy="25" r="24" fill="#fff"/><path d="M13 21h14v-7l12 11-12 11v-7H13z" fill="#f3a800"/></svg>GOLD MEMBERS<br>CLUB LOUNGE</div>
  <div class="promo pink"><div class="icon" role="img" aria-label="Turntable icon" style="border-radius:8px;background:linear-gradient(135deg,#ddd,#777)"></div><svg width="50" height="50"><circle cx="25" cy="25" r="24" fill="#fff"/><path d="M13 21h14v-7l12 11-12 11v-7H13z" fill="#e2138e"/></svg>GET PARTYCARD<br>FOR DISCOUNTS</div>
</div>
</body>
</html>
```